Business Card Design

Mobile dog grooming

Industry/Entity Type

Business

Contact Information for Business Card

Bluefern Mobile Grooming
Marisol Teague
555-314-9072
www.bluefernmobilegrooming.example

```html
<!DOCTYPE html>
<html lang="en">
<head>
<meta charset="UTF-8">
<title>Bluefern Mobile Grooming – Business Card</title>
<link rel="stylesheet" href="https://fonts.googleapis.com/css2?family=Oswald:wght@500&family=Open+Sans:wght@400;600&display=swap">
<style>
  :root {
    --page-bg: #e9e8ec;
    --card-white: #ffffff;
    --brand-purple: #8566ae;
    --text-light: #ffffff;
    --art-blue: #a9d4f0;
    --art-cream: #f1e3c4;
    --art-lilac: #cfc2e6;
  }
  html, body {
    margin: 0;
    width: 1200px;
    height: 900px;
    overflow: hidden;
    background: var(--page-bg);
  }
  .canvas {
    position: relative;
    width: 1200px;
    height: 900px;
    display: flex;
    align-items: center;
    justify-content: center;
  }
  .card {
    position: relative;
    width: 440px;
    height: 770px;
    border-radius: 26px;
    overflow: hidden;
    background: var(--card-white);
    box-shadow: 0 14px 36px rgba(40, 30, 60, 0.22);
  }
  .card__brand {
    position: absolute;
    top: 0; left: 0; right: 0;
    height: 400px;
    display: flex;
    flex-direction: column;
    align-items: center;
    justify-content: center;
  }
  .brand-art {
    width: 340px;
    height: 220px;
    border-radius: 110px 110px 40px 40px;
    background: linear-gradient(135deg, var(--art-blue) 0%, var(--art-cream) 55%, var(--art-lilac) 100%);
  }
  .brand-name {
    margin-top: 18px;
    font-family: "Oswald", sans-serif;
    font-weight: 500;
    font-size: 30px;
    letter-spacing: 1px;
    text-transform: uppercase;
    color: var(--brand-purple);
    text-align: center;
  }
  .card__contact {
    position: absolute;
    top: 400px; left: 0; right: 0;
    height: 240px;
    background: var(--brand-purple);
    text-align: center;
    color: var(--text-light);
  }
  .card__notch {
    position: absolute;
    top: 0;
    left: 50%;
    transform: translateX(-50%);
  }
  .contact-name {
    margin: 58px 0 0;
    font-family: "Oswald", sans-serif;
    font-weight: 500;
    font-size: 40px;
    letter-spacing: 1px;
    text-transform: uppercase;
  }
  .contact-phone {
    margin: 10px 0 0;
    font-family: "Open Sans", sans-serif;
    font-size: 23px;
  }
  .card__web {
    position: absolute;
    top: 648px; left: 0; right: 0;
    height: 56px;
    display: flex;
    align-items: center;
    justify-content: center;
    font-family: "Open Sans", sans-serif;
    font-weight: 600;
    font-size: 19px;
    color: var(--brand-purple);
  }
  .card__footer {
    position: absolute;
    top: 712px; left: 0; right: 0; bottom: 0;
    background: var(--brand-purple);
  }
</style>
</head>
<body>
  <main class="canvas">
    <article class="card">
      <section class="card__brand">
        <div class="brand-art" role="img" aria-label="Illustration of cartoon dogs in a bubbly bath tub on wheels"></div>
        <div class="brand-name">Bluefern Mobile Grooming</div>
      </section>

      <section class="card__contact">
        <svg class="card__notch" width="28" height="14" viewBox="0 0 28 14" aria-hidden="true">
          <polygon points="0,0 28,0 14,14" fill="#ffffff"/>
        </svg>
        <h1 class="contact-name">Marisol Teague</h1>
        <p class="contact-phone">555-314-9072</p>
      </section>

      <div class="card__web">www.bluefernmobilegrooming.example</div>
      <div class="card__footer"></div>
    </article>
  </main>
</body>
</html>
```